Website for Kitchen Showroom

We need a website for our Kitchen Showroom. Will be 10 pages in total. Example of a website we like can be found at http://www.brivantaform.co.uk/ with the image on the front page being a java script slideshow picking up images from a directory that I can update. Looking for simple SEO
I have the wording/ sitemap/ images all ready to go and I am looking for a quick turn around.
Thank you for your time. Tom

```html
<!DOCTYPE html>
<html lang="en">
<head>
<meta charset="utf-8">
<title>Hearthline Kitchens – Designer Kitchens</title>
<link rel="stylesheet" href="https://fonts.googleapis.com/css2?family=Open+Sans:wght@300;400&family=Roboto+Condensed:wght@400&family=Roboto+Slab:wght@900&display=swap">
<style>
:root{
  --page:#25262a;
  --page-deep:#1c1d20;
  --header:#2e2f33;
  --rule:#3b3c40;
  --panel:#3a3b3f;
  --sidebar:#47484c;
  --sidebar-text:#343538;
  --text:#a4a5a8;
  --heading:#e8e8e8;
  --nav:#a9aaad;
  --nav-active:#ffffff;
  --accent:#8dc63f;
  --footer:#2c2d30;
  --footer-text:#8f9093;
}
*{margin:0;padding:0;box-sizing:border-box}
html,body{width:1200px;height:960px;overflow:hidden}
body{background:var(--page);font-family:Arial,Helvetica,sans-serif;position:relative}
.site-header{position:absolute;left:0;top:8px;width:1200px;height:109px;background:var(--header);border-bottom:1px solid var(--rule)}
.brand{position:absolute;left:143px;top:42px;display:flex;align-items:center;gap:10px;font-family:"Open Sans",sans-serif;font-weight:300;font-size:27px;line-height:27px;color:#d4d4d4;width:240px}
.brand-mark{width:26px;height:26px;background:var(--accent);flex:none}
.main-nav{position:absolute;top:62px;left:579px;display:flex;font-size:15px}
.main-nav a{color:var(--nav);text-decoration:none;margin-right:0}
.main-nav a.active{color:var(--nav-active)}
.main-nav a:nth-child(1){width:61px}
.main-nav a:nth-child(2){width:79px}
.main-nav a:nth-child(3){width:80px}
.main-nav a:nth-child(4){width:79px}
.main-nav a:nth-child(5){width:105px}
.content-area{position:absolute;left:143px;top:137px;width:745px;height:773px;background:linear-gradient(var(--panel) 0,var(--page) 420px)}
.slider{position:absolute;left:0;top:0;width:745px;height:415px;background:#525357}
.slide{position:absolute;left:12px;top:14px;width:732px;height:389px;background:linear-gradient(100deg,#cfd1d2 0%,#8a8c8f 35%,#3d3e40 60%,#6a6b6e 85%,#9a9b9d 100%)}
.slider-arrow{position:absolute;top:175px;width:28px;height:33px;background:#4a4b4f}
.slider-arrow.prev{left:12px}
.slider-arrow.next{left:716px}
.intro{position:absolute;left:0;top:448px;width:700px}
.intro h1{font-family:"Roboto Condensed",sans-serif;font-weight:400;font-size:22px;color:var(--heading);margin-bottom:18px}
.intro p{font-size:12px;line-height:18px;color:var(--text);margin-bottom:18px}
.intro .lead{color:var(--accent);font-size:13.5px}
.sidebar{position:absolute;left:888px;top:137px;width:137px;height:773px;background:var(--sidebar)}
.sidebar-title{position:absolute;left:83px;top:40px;transform-origin:0 0;transform:rotate(-90deg) translate(-560px,-50px);font-family:"Roboto Slab",serif;font-weight:900;font-size:54px;color:var(--sidebar-text);white-space:nowrap;width:560px;text-align:right}
.social{position:absolute;left:48px;top:745px;display:flex;gap:8px}
.social span{width:16px;height:16px;display:block}
.social .one{background:#5aa7c9}
.social .two{background:#4a66a0}
.site-footer{position:absolute;left:0;top:913px;width:1200px;height:40px;background:var(--footer);border-top:1px solid #38393c;font-size:10.5px;color:var(--footer-text)}
.footer-links{position:absolute;left:143px;top:15px}
.footer-links a{color:var(--footer-text);text-decoration:none}
.copyright{position:absolute;right:175px;top:14px}
.page-base{position:absolute;left:0;top:953px;width:1200px;height:7px;background:var(--page-deep)}
</style>
</head>
<body>
<header class="site-header">
  <div class="brand"><span class="brand-mark"></span><span>hearthline kitchens</span></div>
  <nav class="main-nav">
    <a class="active" href="#">Home</a><a href="#">Design</a><a href="#">Gallery</a><a href="#">Quality</a><a href="#">Contact Us</a><a href="#">Links</a>
  </nav>
</header>

<main class="content-area">
  <div class="slider">
    <div class="slide" role="img" aria-label="Modern dark wood kitchen with dining table and pendant lamps"></div>
    <svg class="slider-arrow prev" viewBox="0 0 28 33"><path d="M17 9 L10 16.5 L17 24" fill="none" stroke="#fff" stroke-width="3"/></svg>
    <svg class="slider-arrow next" viewBox="0 0 28 33"><path d="M11 9 L18 16.5 L11 24" fill="none" stroke="#fff" stroke-width="3"/></svg>
  </div>
  <section class="intro">
    <h1>Designer Kitchens by Hearthline Kitchens</h1>
    <p><span class="lead">Welcome to Hearthline Kitchens.</span> The region's exclusive kitchen manufacturer based in Westmere Bay. If you are seeking the highest quality kitchen, yet at a price that is a little more affordable, Hearthline Kitchens is the company you've been searching for.</p>
    <p>Hearthline Kitchens showroom is located less than 25 kilometers from the city centre, so easy to get to with easy access from the Coastal Highway.</p>
    <p>On this site, you can view some of our designer kitchens, read testimonials from our clients or just browse through our site to find out more. We hope you will find our site inspiring and put Hearthline Kitchens at the top of your list of kitchen showrooms you simply must visit.</p>
    <p>Pop into our showroom. We can chat about your plans and ideas for your new kitchen and maybe we can give you a few ideas of our own. Or contact us to arrange a no obligation consultation with one of our kitchen designers and if required we will bring the showroom to you.</p>
  </section>
</main>

<aside class="sidebar">
  <div class="sidebar-title">Designer Kitchens</div>
  <div class="social"><span class="one"></span><span class="two"></span></div>
</aside>

<footer class="site-footer">
  <div class="footer-links"><a href="#">Site Map</a> &nbsp;I <a href="#">Privacy Policy</a> I <a href="#">Gallery</a> I <a href="#">Contact Us</a></div>
  <div class="copyright">© 2011 Hearthline Kitchens. All right reserved.</div>
</footer>
<div class="page-base"></div>
</body>
</html>
```